WordPress Website Design - Brennick Auction

Need a WordPress design for an auction company wanting a responsive, simple and easy to use site. Current site to be upgraded: http://www.brennickauctions.example/

A site the client mentions liking is http://www.taverlyauction.example. The attached logo color can be changed to suit your design - a different red, or green perhaps.

Industry/Entity Type

It Company

Number of Pages Required

1 page

Font styles to use
Serif
Sans Serif

Requirements
Must have
• Keep in mind this site will be built on a responsive theme.
• Site navigation: 1) Home, 2) Auctions, 3) Real Estate Listings, 4) Services, 5) Appraisals, 6) The Gavel Hall, 7) About Us, 8) Contact Us
• Site will have large, prominent full width (960px) slideshow - please pick one of the 3 attached images. Colors can be different than current site - wants a brighter site, colors complementing the logo. Home page will have auction list (the look of the auction list can be seen at http://www.northgateholdingsweb.example/auction-calendar/)
• The widgets in the sidebar/header are: Email signup form, social media(FB Twitter, Youtube), News & Events blog, Testimonials, Featured Auctions, Featured Listings widget.
• Footer will have smaller company logo(below), contact info, and attached association logos.
• Gordon Brennick Auction-Realty
• 3817 Pelham Court • Castor Falls, IN 47088
• dominic@brennickauctions.example
• 812.555.0146
• 877.555.0193
Nice to have
• Design of dropdown menus: under Auctions, 1) Current Auctions, 2) Online Auctions, 3) Past Auctions

```html
<!DOCTYPE html>
<html lang="en">
<head>
<meta charset="utf-8">
<title>Brennick Auction</title>
<link rel="stylesheet" href="https://fonts.googleapis.com/css2?family=Open+Sans:wght@400;600;700;800&display=swap">
<style>
:root{
  --red:#e0334a;
  --ink:#2d2d2d;
  --dark:#3a3a3a;
  --darker:#2b2b2b;
  --grey:#7d7d7d;
  --light:#f1f1f1;
  --line:#e2e2e2;
  --white:#ffffff;
}
*{box-sizing:border-box;margin:0;padding:0}
html,body{width:1200px;height:2612px;overflow:hidden}
body{font-family:"Open Sans",Arial,sans-serif;color:var(--ink);background:var(--light);position:relative}
.wrap{width:1000px;margin:0 auto;position:relative}

/* header */
.site-header{height:88px;background:var(--white)}
.site-header .wrap{display:flex;justify-content:space-between;align-items:center;height:88px}
.brand{font-size:26px;font-weight:700;color:var(--ink);letter-spacing:0}
.header-right{display:flex;align-items:center;gap:18px;font-size:13px;color:var(--red)}
.mini-social{display:flex;gap:8px}
.mini-social span{width:12px;height:12px;background:#9a9a9a;border-radius:2px}

.main-nav{height:28px;background:var(--dark)}
.main-nav ul{list-style:none;display:flex;width:1000px;margin:0 auto}
.main-nav li{font-size:11px;color:#ddd;padding:0 17px;line-height:28px}
.main-nav li.active{background:var(--red);color:#fff}

/* hero */
.hero{height:572px;position:relative;background:linear-gradient(180deg,#b9cfe6 0%,#d9e3ea 35%,#6d7f58 60%,#56703c 100%)}
.hero-photo{position:absolute;inset:0}
.hero-caption{position:absolute;left:100px;top:356px;width:300px;background:rgba(30,30,30,.82);padding:20px 18px}
.hero-caption h2{color:#fff;font-size:22px;font-weight:700;line-height:1.3}
.hero-caption p{color:#ccc;font-size:10px;margin-top:10px;line-height:1.5}
.hero-arrow{position:absolute;top:266px;width:22px;height:40px;background:rgba(0,0,0,.35);display:flex;align-items:center;justify-content:center}
.hero-arrow.prev{left:0}.hero-arrow.next{right:0}

/* content */
.content{display:flex;justify-content:space-between;padding-top:56px}
.listings{width:720px}
.section-title{font-size:26px;font-weight:600;margin-bottom:20px;padding-left:2px}
.listing{background:var(--white);height:262px;margin-bottom:42px;padding:28px 28px;position:relative;box-shadow:0 1px 2px rgba(0,0,0,.06)}
.listing-photo{position:absolute;left:28px;top:40px;width:152px;height:158px;background:linear-gradient(180deg,#9fc1e3 0%,#c9d6c4 45%,#6d8f45 100%)}
.listing-body{margin-left:200px}
.listing h3{font-size:15px;font-weight:700;line-height:1.3}
.listing p{font-size:9.5px;color:var(--grey);line-height:1.55;margin-top:8px}
.listing .type{font-size:10px;font-weight:700;margin-top:8px}
.listing .meta{display:flex;gap:34px;font-size:9.5px;color:var(--grey);margin-top:8px;align-items:center}
.listing .meta b{color:var(--ink)}
.listing .actions{position:absolute;right:28px;bottom:26px;display:flex;gap:6px}
.btn{width:100px;height:24px;font-size:10px;font-weight:700;color:#fff;display:flex;align-items:center;justify-content:center}
.btn.details{background:var(--red)}
.btn.photos{background:var(--dark)}

.pagination{display:flex;justify-content:center;gap:6px;margin-top:-8px;padding-left:220px}
.pagination span{width:22px;height:22px;background:var(--white);border:1px solid var(--line);font-size:10px;display:flex;align-items:center;justify-content:center;color:var(--grey)}
.pagination span.current{background:var(--red);color:#fff;border-color:var(--red)}

/* sidebar */
.sidebar{width:232px}
.widget-title-plain{font-size:11px;font-weight:700}
.social-row{display:flex;gap:6px;margin-top:12px;margin-bottom:26px}
.social-row span{width:28px;height:28px;border-radius:3px}
.widget{background:var(--white);margin-bottom:24px;box-shadow:0 1px 2px rgba(0,0,0,.06)}
.widget h4{background:var(--red);color:#fff;font-size:11px;font-weight:700;padding:9px 12px}
.widget .inner{padding:14px 12px}
.field{height:26px;border:1px solid var(--line);font-size:9px;color:#aaa;padding:6px 8px;margin-bottom:8px}
.subscribe-btn{width:74px;height:24px;background:var(--dark);color:#fff;font-size:9px;font-weight:700;display:flex;align-items:center;justify-content:center;margin-left:auto}
.news-item{display:flex;gap:8px;margin-bottom:14px}
.news-item svg{flex:none;margin-top:2px}
.news-item a{font-size:10px;color:var(--red);line-height:1.45;text-decoration:none;display:block}
.news-item small{font-size:8.5px;color:#aaa;display:block;margin-top:3px}
.feat-item{display:flex;gap:10px;margin-bottom:14px}
.feat-thumb{width:46px;height:40px;flex:none;background:linear-gradient(180deg,#a8c5e4,#7a9b55)}
.feat-item a{font-size:10px;color:var(--red);line-height:1.45;text-decoration:none}
.testi{display:flex;gap:10px;margin-bottom:16px}
.avatar{width:40px;height:40px;border-radius:50%;background:linear-gradient(180deg,#b7c3cf,#7e8a96);flex:none}
.testi p{font-size:10px;color:var(--red);line-height:1.45}
.testi small{font-size:8.5px;color:#aaa}

/* newsletter band */
.newsletter-band{position:absolute;left:0;top:2140px;width:1200px;height:64px;background:var(--red)}
.newsletter-band .wrap{display:flex;align-items:center;justify-content:space-between;height:64px}
.nl-form{display:flex;align-items:center;gap:8px}
.nl-input{width:250px;height:26px;background:#fff;font-size:9px;color:#aaa;padding:7px 10px}
.nl-btn{height:26px;padding:0 14px;border:1px solid rgba(255,255,255,.7);color:#fff;font-size:9px;font-weight:700;display:flex;align-items:center}
.band-social{display:flex;gap:8px}
.band-social span{width:26px;height:26px;border:1px solid rgba(255,255,255,.8);border-radius:2px}

/* footer */
.site-footer{position:absolute;left:0;top:2204px;width:1200px;height:356px;background:var(--white)}
.site-footer .wrap{display:flex;padding-top:46px}
.foot-brand{width:420px}
.foot-brand .brand{font-size:22px}
.foot-brand ul{list-style:none;margin-top:14px}
.foot-brand li{font-size:10px;color:var(--grey);line-height:1.75;display:flex;align-items:center;gap:6px}
.foot-brand li i{width:7px;height:7px;background:var(--red);border-radius:50%;display:inline-block}
.associations{width:360px;text-align:center}
.associations h5,.foot-menu h5{font-size:13px;font-weight:700}
.badges{display:flex;gap:16px;justify-content:center;margin-top:44px}
.badges span{width:48px;height:48px;background:#3b3b3b}
.badges span.round{border-radius:50%}
.foot-menu{margin-left:auto;width:120px}
.foot-menu ul{list-style:none;margin-top:12px}
.foot-menu li{font-size:10px;color:var(--grey);line-height:1.6}
.bottom-bar{position:absolute;left:0;top:2560px;width:1200px;height:52px;background:var(--darker);color:#9a9a9a;font-size:9px;display:flex;align-items:center;justify-content:center}
.bottom-bar .top{position:absolute;right:100px;width:24px;height:22px;background:#444}
</style>
</head>
<body>

<header class="site-header">
  <div class="wrap">
    <div class="brand">Brennick Auction</div>
    <div class="header-right">
      <span>Subscribe to Newsletter</span>
      <div class="mini-social"><span></span><span></span><span></span><span></span></div>
    </div>
  </div>
</header>

<nav class="main-nav">
  <ul>
    <li class="active">Home</li><li>Auctions</li><li>Real Estate Listings</li><li>Services</li><li>Appraisals</li><li>The Gavel Hall</li><li>About Us</li><li>Contact Us</li>
  </ul>
</nav>

<section class="hero">
  <div class="hero-photo" role="img" aria-label="Photo of a large two-storey brick family home with lawn and trees under a blue sky"></div>
  <div class="hero-arrow prev"><svg width="10" height="14"><path d="M8 1 2 7l6 6" stroke="#fff" stroke-width="2" fill="none"/></svg></div>
  <div class="hero-arrow next"><svg width="10" height="14"><path d="M2 1l6 6-6 6" stroke="#fff" stroke-width="2" fill="none"/></svg></div>
  <div class="hero-caption">
    <h2>Lorem ipsum dolor sit amet, con sectetur adipiscing elit.</h2>
    <p>Aliquam nec libero tincidunt dui, pharetra gravida massa. Quisque auctor elit eget augue ornare.</p>
  </div>
</section>

<main class="wrap content">
  <section class="listings">
    <h1 class="section-title">Auction Listings</h1>

    <article class="listing">
      <div class="listing-photo" role="img" aria-label="Photo of a suburban house listed for auction"></div>
      <div class="listing-body">
        <h3>Duis eu lacinia risus. Nullam scelerisque dium libero in blandit. Donec laoreet ac lacus</h3>
        <p>Lorem ipsum dolor sit amet, adipiscing elit. Nulla tincidunt felis non metus vestibulum, sed pretium lacus consequat. Morbi vel purus quis magna feugiat dictum. Etiam ac orci ut erat aliquet semper et vitae.</p>
        <div class="type">LIVE ON SITE AUCTION LOCATION</div>
        <div class="meta"><span><svg width="8" height="10"><path d="M4 0a4 4 0 0 1 4 4c0 3-4 6-4 6S0 7 0 4a4 4 0 0 1 4-4z" fill="#999"/></svg> Lorem ipsum dolor</span><span><b>BEGINS:</b> 08/21/14 AT 7:00 PM EST</span></div>
      </div>
      <div class="actions"><span class="btn details">DETAILS</span><span class="btn photos">PHOTOS</span></div>
    </article>

    <article class="listing">
      <div class="listing-photo" role="img" aria-label="Photo of a stucco villa listed for auction"></div>
      <div class="listing-body">
        <h3>Duis eu lacinia risus. Nullam scelerisque dium libero in blandit. Donec laoreet ac lacus</h3>
        <p>Lorem ipsum dolor sit amet, adipiscing elit. Nulla tincidunt felis non metus vestibulum, sed pretium lacus consequat. Morbi vel purus quis magna feugiat dictum. Etiam ac orci ut erat aliquet semper et vitae.</p>
        <div class="type">LIVE ON SITE AUCTION LOCATION</div>
        <div class="meta"><span><svg width="8" height="10"><path d="M4 0a4 4 0 0 1 4 4c0 3-4 6-4 6S0 7 0 4a4 4 0 0 1 4-4z" fill="#999"/></svg> Lorem ipsum dolor</span><span><b>BEGINS:</b> 08/21/14 AT 7:00 PM EST</span></div>
      </div>
      <div class="actions"><span class="btn details">DETAILS</span><span class="btn photos">PHOTOS</span></div>
    </article>

    <article class="listing">
      <div class="listing-photo" role="img" aria-label="Photo of a blue-sided family home listed for auction"></div>
      <div class="listing-body">
        <h3>Duis eu lacinia risus. Nullam scelerisque dium libero in blandit. Donec laoreet ac lacus</h3>
        <p>Lorem ipsum dolor sit amet, adipiscing elit. Nulla tincidunt felis non metus vestibulum, sed pretium lacus consequat. Morbi vel purus quis magna feugiat dictum. Etiam ac orci ut erat aliquet semper et vitae.</p>
        <div class="type">LIVE ON SITE AUCTION LOCATION</div>
        <div class="meta"><span><svg width="8" height="10"><path d="M4 0a4 4 0 0 1 4 4c0 3-4 6-4 6S0 7 0 4a4 4 0 0 1 4-4z" fill="#999"/></svg> Lorem ipsum dolor</span><span><b>BEGINS:</b> 08/21/14 AT 7:00 PM EST</span></div>
      </div>
      <div class="actions"><span class="btn details">DETAILS</span><span class="btn photos">PHOTOS</span></div>
    </article>

    <article class="listing">
      <div class="listing-photo" role="img" aria-label="Photo of a ranch house with lawn listed for auction"></div>
      <div class="listing-body">
        <h3>Duis eu lacinia risus. Nullam scelerisque dium libero in blandit. Donec laoreet ac lacus</h3>
        <p>Lorem ipsum dolor sit amet, adipiscing elit. Nulla tincidunt felis non metus vestibulum, sed pretium lacus consequat. Morbi vel purus quis magna feugiat dictum. Etiam ac orci ut erat aliquet semper et vitae.</p>
        <div class="type">LIVE ON SITE AUCTION LOCATION</div>
        <div class="meta"><span><svg width="8" height="10"><path d="M4 0a4 4 0 0 1 4 4c0 3-4 6-4 6S0 7 0 4a4 4 0 0 1 4-4z" fill="#999"/></svg> Lorem ipsum dolor</span><span><b>BEGINS:</b> 08/21/14 AT 7:00 PM EST</span></div>
      </div>
      <div class="actions"><span class="btn details">DETAILS</span><span class="btn photos">PHOTOS</span></div>
    </article>

    <nav class="pagination"><span>&lsaquo;</span><span>1</span><span class="current">2</span><span>3</span><span>4</span><span>5</span><span>&rsaquo;</span></nav>
  </section>

  <aside class="sidebar">
    <div class="widget-title-plain">SOCIAL MEDIA</div>
    <div class="social-row">
      <span style="background:#3b5998"></span><span style="background:#d34836"></span><span style="background:#c4302b"></span><span style="background:#33a8e0"></span>
    </div>

    <section class="widget">
      <h4>SUBSCRIBE</h4>
      <div class="inner">
        <div class="field">Name</div>
        <div class="field">Email</div>
        <div class="subscribe-btn">SUBSCRIBE</div>
      </div>
    </section>

    <section class="widget">
      <h4>NEWS &amp; EVENTS BLOG</h4>
      <div class="inner">
        <div class="news-item"><svg width="8" height="10"><path d="M1 1l5 4-5 4" stroke="#e0334a" stroke-width="2" fill="none"/></svg><div><a>Vivamus at elit quis urna adipiscing iaculis.</a><small>26 May 2014</small></div></div>
        <div class="news-item"><svg width="8" height="10"><path d="M1 1l5 4-5 4" stroke="#e0334a" stroke-width="2" fill="none"/></svg><div><a>Curabitur vitae velit</a><small>26 May 2014</small></div></div>
        <div class="news-item"><svg width="8" height="10"><path d="M1 1l5 4-5 4" stroke="#e0334a" stroke-width="2" fill="none"/></svg><div><a>Vivamus at elit quis urna adipiscing iaculis.</a><small>26 May 2014</small></div></div>
        <div class="news-item"><svg width="8" height="10"><path d="M1 1l5 4-5 4" stroke="#e0334a" stroke-width="2" fill="none"/></svg><div><a>Curabitur vitae velit</a><small>26 May 2014</small></div></div>
      </div>
    </section>

    <section class="widget">
      <h4>FEATURED AUCTIONS</h4>
      <div class="inner">
        <div class="feat-item"><div class="feat-thumb" role="img" aria-label="Thumbnail photo of a featured property"></div><a>Vivamus at elit quis urna adipiscing iaculis.</a></div>
        <div class="feat-item"><div class="feat-thumb" role="img" aria-label="Thumbnail photo of a featured property"></div><a>Vivamus at elit quis urna adipiscing iaculis.</a></div>
        <div class="feat-item"><div class="feat-thumb" role="img" aria-label="Thumbnail photo of a featured property"></div><a>Vivamus at elit quis urna adipiscing iaculis.</a></div>
      </div>
    </section>

    <section class="widget">
      <h4>TESTIMONIALS</h4>
      <div class="inner">
        <div class="testi"><div class="avatar" role="img" aria-label="Client portrait"></div><div><p>Vivamus at elit quis urna adipiscing iaculis.</p><small>Jane Doe</small></div></div>
        <div class="testi"><div class="avatar" role="img" aria-label="Client portrait"></div><div><p>Vivamus at elit quis urna adipiscing iaculis.</p><small>John Doe</small></div></div>
        <div class="testi"><div class="avatar" role="img" aria-label="Client portrait"></div><div><p>Vivamus at elit quis urna adipiscing iaculis.</p><small>Jane Doe</small></div></div>
      </div>
    </section>
  </aside>
</main>

<section class="newsletter-band">
  <div class="wrap">
    <div class="nl-form"><div class="nl-input">Enter your email here</div><div class="nl-btn">SUBSCRIBE</div></div>
    <div class="band-social"><span></span><span></span><span></span><span></span></div>
  </div>
</section>

<footer class="site-footer">
  <div class="wrap">
    <div class="foot-brand">
      <div class="brand">Brennick Auction</div>
      <ul>
        <li><i></i>Gordon Brennick Auction-Realty</li>
        <li><i></i>3817 Pelham Court &bull; Castor Falls, IN 47088</li>
        <li><i></i>dominic@brennickauctions.example</li>
        <li><i></i>812.555.0146</li>
        <li><i></i>877.555.0193</li>
      </ul>
    </div>
    <div class="associations">
      <h5>Associations</h5>
      <div class="badges"><span></span><span class="round"></span><span></span><span class="round"></span></div>
    </div>
    <div class="foot-menu">
      <h5>Menu</h5>
      <ul><li>Home</li><li>Auctions</li><li>Real Estate Listings</li><li>Services</li><li>Appraisals</li><li>The Gavel Hall</li><li>About Us</li><li>Contact Us</li></ul>
    </div>
  </div>
</footer>

<div class="bottom-bar">&copy; 2014 Brennick Auction. All Rights Reserved.<span class="top"></span></div>

</body>
</html>
```